Desktop Wallpaper for Tech Company

We need a graphic designer to come up with a PC desktop wallpaper to rollout to numerous computers managed by our business. We are a technology consultancy firm based in Perth, Western Australia that provides a number of IT services including datacentre/cloud services, software development, cyber security, managed services and more.

The vibe for this desktop wallpaper must be aligned with innovation, cutting edge, technology, cyber, revolutionary. When people see PC wallpaper it should scream "cutting edge" tech company.

With regards to the contents of the image, this is up to the designer however we would like to ask our logo to be featured in the design somewhere (we uploaded two different logo samples of different layout in vector format).

This wallpaper will go on numerous computers so we would like both 4:3 version as well as widescreen in the following dimensions:

4:3
1024 x 768
1440 x 1080
2048 x 1536

Widescreen:
HD: 1920 x 1080
UHD: 2560×1440
4K: 3840 x 2160
8K: 7680 x 4320

We will be using this wallpaper for both the Desktop Wallpaper and Windows 10 Lockscreen. Please be aware of the following items that will overlap the design by the Windows 10 operating system so be mindful of this when mapping out the design:
- Start Menu
- Desktop Icons that are generally on the LEFT of the screen
- Windows 10 Lockscreen has items on both the bottom left and right of the screen.

At the top right of the design we would like the following phone number and email address to be included so users have the support contact details:

Phone 08 9312 4086
Email support@fernquillsystemsgroup.com.au

We are really looking forward to seeing the designs posted for this competition.

```html
<!DOCTYPE html>
<html lang="en">
<head>
<meta charset="utf-8">
<title>Fernquill Systems — Desktop Wallpaper</title>
<link rel="stylesheet" href="https://fonts.googleapis.com/css2?family=Orbitron:wght@400;800&family=Poppins:wght@500&display=swap">
<style>
  :root {
    --sheet-top: #f3f3f3;
    --sheet-grey: #a9b2bc;
    --night: #02041a;
    --navy: #061066;
    --royal: #0d2fb3;
    --glow: #2f7dff;
    --azure: #1f8bff;
    --white: #ffffff;
    --icon-blue: #3aa0ff;
  }
  * { box-sizing: border-box; margin: 0; padding: 0; }
  html, body { width: 1200px; height: 2400px; overflow: hidden; }
  body { position: relative; background: var(--sheet-grey); }

  .sheet-top {
    position: absolute; left: 0; top: 0; width: 1200px; height: 1055px;
    background: var(--sheet-top);
  }

  .wallpaper {
    position: absolute; overflow: hidden;
    background:
      radial-gradient(ellipse 55% 9% at var(--cx) var(--band), rgba(80,150,255,.75), rgba(40,100,255,.25) 45%, transparent 80%),
      radial-gradient(ellipse 70% 35% at var(--cx) calc(var(--band) + 14%), rgba(20,70,220,.45), transparent 70%),
      radial-gradient(ellipse 60% 55% at 70% 20%, rgba(12,30,140,.55), transparent 75%),
      linear-gradient(100deg, var(--night) 0%, var(--navy) 45%, #0a1680 70%, var(--navy) 100%);
  }
  .wallpaper--screen { left: 240px; top: 254px; width: 729px; height: 440px; font-size: 8.6px; --cx: 58%; --band: 59%; --brand-top: 53%; --headline-top: 64%; }
  .wallpaper--standard { left: 206px; top: 1129px; width: 789px; height: 592px; font-size: 10px; --cx: 58%; --band: 59%; --brand-top: 51.5%; --headline-top: 61.8%; }
  .wallpaper--wide { left: 206px; top: 1796px; width: 789px; height: 444px; font-size: 8.3px; --cx: 64.5%; --band: 58%; --brand-top: 53%; --headline-top: 63%; }

  .support {
    position: absolute; top: var(--support-top, 6.5%); left: var(--support-left, 57.8%);
    font-family: "Poppins", sans-serif; font-weight: 500; color: var(--white);
    font-size: 1.35em; line-height: 1.3;
  }
  .wallpaper--screen .support { --support-top: 7%; --support-left: 57.5%; }
  .wallpaper--wide .support { --support-top: 7.6%; --support-left: 65%; }
  .support__row { display: flex; align-items: center; gap: .45em; }
  .support__icon { width: 1em; height: 1em; flex: none; }

  .brand {
    position: absolute; left: var(--cx); top: var(--brand-top);
    transform: translateX(-50%);
    display: flex; align-items: center; gap: .6em; white-space: nowrap;
    font-family: "Orbitron", sans-serif; font-weight: 800; color: var(--white);
    font-size: 1.75em; letter-spacing: .03em; line-height: 1;
  }
  .brand__mark { width: .6em; height: .6em; background: var(--azure); flex: none; }

  .headline {
    position: absolute; left: var(--cx); top: var(--headline-top);
    transform: translateX(-50%);
    font-family: "Orbitron", sans-serif; font-size: 1em; text-align: center; white-space: nowrap;
    line-height: 1.02;
  }
  .headline__line { display: block; }
  .headline__line--light { font-weight: 400; font-size: 3.9em; color: var(--white); }
  .headline__line--bold { font-weight: 800; font-size: 3.7em; color: var(--white); letter-spacing: .02em; }
  .headline__line--accent { font-weight: 800; font-size: 3.9em; color: var(--azure); letter-spacing: .02em; }
</style>
</head>
<body>
  <div class="sheet-top"></div>

  <section class="wallpaper wallpaper--screen" aria-label="Desktop wallpaper, screen view">
    <div class="support">
      <div class="support__row"><svg class="support__icon" viewBox="0 0 20 20"><circle cx="10" cy="10" r="10" fill="var(--icon-blue)"/><path d="M6.5 5.2l1.8-.3 1 2.4-1.1.9c.6 1.3 1.6 2.3 2.9 2.9l.9-1.1 2.4 1-.3 1.8c-4.2.3-7.9-3.4-7.6-7.6z" fill="var(--white)"/></svg>08 9312 4086</div>
      <div class="support__row"><svg class="support__icon" viewBox="0 0 20 20"><circle cx="10" cy="10" r="10" fill="var(--icon-blue)"/><rect x="5" y="6.5" width="10" height="7" rx="1" fill="var(--white)"/><path d="M5.5 7l4.5 3.4L14.5 7" stroke="var(--icon-blue)" stroke-width="1.1" fill="none"/></svg>support@fernquillsystemsgroup.com.au</div>
    </div>
    <div class="brand"><span class="brand__mark"></span>FERNQUILL SYSTEMS</div>
    <h1 class="headline">
      <span class="headline__line headline__line--light">PUSHING THE</span>
      <span class="headline__line headline__line--bold">BOUNDARIES OF</span>
      <span class="headline__line headline__line--accent">TECHNOLOGY</span>
    </h1>
  </section>

  <section class="wallpaper wallpaper--standard" aria-label="Desktop wallpaper, 4:3 version">
    <div class="support">
      <div class="support__row"><svg class="support__icon" viewBox="0 0 20 20"><circle cx="10" cy="10" r="10" fill="var(--icon-blue)"/><path d="M6.5 5.2l1.8-.3 1 2.4-1.1.9c.6 1.3 1.6 2.3 2.9 2.9l.9-1.1 2.4 1-.3 1.8c-4.2.3-7.9-3.4-7.6-7.6z" fill="var(--white)"/></svg>08 9312 4086</div>
      <div class="support__row"><svg class="support__icon" viewBox="0 0 20 20"><circle cx="10" cy="10" r="10" fill="var(--icon-blue)"/><rect x="5" y="6.5" width="10" height="7" rx="1" fill="var(--white)"/><path d="M5.5 7l4.5 3.4L14.5 7" stroke="var(--icon-blue)" stroke-width="1.1" fill="none"/></svg>support@fernquillsystemsgroup.com.au</div>
    </div>
    <div class="brand"><span class="brand__mark"></span>FERNQUILL SYSTEMS</div>
    <h1 class="headline">
      <span class="headline__line headline__line--light">PUSHING THE</span>
      <span class="headline__line headline__line--bold">BOUNDARIES OF</span>
      <span class="headline__line headline__line--accent">TECHNOLOGY</span>
    </h1>
  </section>

  <section class="wallpaper wallpaper--wide" aria-label="Desktop wallpaper, widescreen version">
    <div class="support">
      <div class="support__row"><svg class="support__icon" viewBox="0 0 20 20"><circle cx="10" cy="10" r="10" fill="var(--icon-blue)"/><path d="M6.5 5.2l1.8-.3 1 2.4-1.1.9c.6 1.3 1.6 2.3 2.9 2.9l.9-1.1 2.4 1-.3 1.8c-4.2.3-7.9-3.4-7.6-7.6z" fill="var(--white)"/></svg>08 9312 4086</div>
      <div class="support__row"><svg class="support__icon" viewBox="0 0 20 20"><circle cx="10" cy="10" r="10" fill="var(--icon-blue)"/><rect x="5" y="6.5" width="10" height="7" rx="1" fill="var(--white)"/><path d="M5.5 7l4.5 3.4L14.5 7" stroke="var(--icon-blue)" stroke-width="1.1" fill="none"/></svg>support@fernquillsystemsgroup.com.au</div>
    </div>
    <div class="brand"><span class="brand__mark"></span>FERNQUILL SYSTEMS</div>
    <h1 class="headline">
      <span class="headline__line headline__line--light">PUSHING THE</span>
      <span class="headline__line headline__line--bold">BOUNDARIES OF</span>
      <span class="headline__line headline__line--accent">TECHNOLOGY</span>
    </h1>
  </section>
</body>
</html>
```